Startup Burlesque Dance Company needs logo and website

Hello designers,
We need a logo design and a website design. The company name is "Velluta Strambo". This is a rough cut of one of the company's shows: http://clipvault.example/kQ7rTmLp2Zd
The design will be for a startup Burlesque dance company. The logo and website should have a simple, retro, vintage "black and white" movie feel to it. The primary purpose for the site is for marketing the dance services, highlighting pictures and video of the show(s). There will be seven basic web pages.
• Home
• About
• Shows
• Company
• Gallery
• Promo Reel
• Contact
The following links are two examples of sites we like, but since this is a competitor, the design should not be identical. It should only serve as an example of the requested style.
http://pennybrassrevue.example/index.cfm
http://www.crookedlampcabaret.example/
In Summary, we will need the following:
1. Logo (example of ones we like are attached in Word file)
2. Web Site Design
3. Stationary ready design for business cards and letterhead
Please design to the following screen size & resolution: 1024 x 768
Reason: Decision maker has been traveling on business so our team has not been able to meet with her.
Target Market(s)
Male and Female, 21-45 years of age
Industry/Entity Type
Marketing
Look and feel

```html
<!DOCTYPE html>
<html lang="en">
<head>
<meta charset="utf-8">
<title>Velluta Strambo — Home</title>
<link href="https://fonts.googleapis.com/css2?family=Cabin:wght@400;600;700&family=Happy+Monkey&display=swap" rel="stylesheet">
<style>
  :root {
    --pink: #f0386f;
    --pink-deep: #d2245a;
    --pink-edge: #b8284f;
    --bar: #151515;
    --ink: #0a0a0a;
    --cream: #ece5e0;
    --nav-text: #d8d8d8;
    --footer-text: #454545;
    --icon: #5a5a5a;
  }
  * { box-sizing: border-box; margin: 0; padding: 0; }
  html, body { width: 1200px; height: 704px; overflow: hidden; background: var(--ink); }
  body { position: relative; font-family: "Cabin", Arial, sans-serif; }

  .top-rule, .bottom-rule { position: absolute; left: 0; width: 1200px; background: var(--pink); }
  .top-rule { top: 0; height: 7px; }
  .bottom-rule { top: 696px; height: 8px; }

  .stage-photo {
    position: absolute; left: 0; top: 7px; width: 1200px; height: 643px;
    background:
      radial-gradient(ellipse 260px 300px at 60px 420px, rgba(190,60,40,.55), transparent 70%),
      radial-gradient(ellipse 240px 260px at 1150px 520px, rgba(200,60,50,.5), transparent 70%),
      radial-gradient(ellipse 300px 160px at 1000px 60px, rgba(60,80,200,.55), transparent 70%),
      radial-gradient(ellipse 200px 200px at 470px 60px, rgba(60,200,140,.35), transparent 70%),
      radial-gradient(ellipse 300px 120px at 1130px 200px, rgba(70,200,170,.35), transparent 70%),
      #0b0b0d;
  }

  .brand {
    position: absolute; left: 149px; top: 30px;
    display: flex; align-items: center; gap: 10px;
  }
  .brand-dot { width: 22px; height: 22px; border-radius: 50%; background: var(--pink); }
  .brand-name { font-weight: 700; font-size: 40px; color: var(--pink); letter-spacing: .5px; line-height: 1; }

  .search {
    position: absolute; left: 888px; top: 61px; width: 173px; height: 30px;
    background: #fff; border: 1px solid #333; border-radius: 3px;
    display: flex; align-items: center; justify-content: space-between; padding: 0 8px 0 10px;
  }
  .search span { font-size: 12px; color: #aaa; }

  .main-nav {
    position: absolute; left: 146px; top: 114px; width: 915px; height: 37px;
    background: var(--bar); border-radius: 3px;
  }
  .main-nav a {
    position: absolute; top: 6px; height: 25px; line-height: 25px;
    font-size: 13.5px; color: var(--nav-text); text-decoration: none; transform: translateX(-50%);
  }
  .main-nav a.current {
    background: var(--pink); color: #fff; width: 80px; text-align: center; border-radius: 3px;
  }

  .feature-panel {
    position: absolute; left: 144px; top: 154px; width: 919px; height: 490px;
    background: var(--pink-edge); border-radius: 12px;
  }
  .feature-inner {
    position: absolute; left: 14px; top: 14px; width: 892px; height: 463px; background: var(--pink);
  }

  .section-links a {
    position: absolute; left: 0; height: 42px; background: var(--pink-deep);
    font-family: "Happy Monkey", cursive; font-size: 36px; line-height: 42px;
    letter-spacing: 7px; color: var(--cream); text-decoration: none; padding-left: 18px;
  }

  .ticket-art {
    position: absolute; left: 18px; top: 271px; width: 403px; height: 162px;
    background: linear-gradient(90deg, #f07aa0, #ecd9b8 30%, #f2e4c8 50%, #ecd9b8 70%, #f07aa0);
    display: flex; align-items: flex-end; justify-content: center; padding-bottom: 14px;
  }
  .ticket-art span {
    font-family: "Happy Monkey", cursive; font-size: 26px; letter-spacing: 3px; color: var(--pink-deep);
  }
  .stage-shot {
    position: absolute; left: 450px; top: 28px; width: 406px; height: 405px;
    background: radial-gradient(ellipse at 55% 45%, #7a7a7a, #3a3a3a 55%, #1f1f1f);
  }

  .site-footer {
    position: absolute; left: 146px; top: 669px; font-size: 12px; font-weight: 600; color: var(--footer-text);
  }
  .social { position: absolute; top: 667px; width: 21px; height: 21px; background: var(--icon); border-radius: 2px; }
</style>
</head>
<body>
  <div class="top-rule"></div>
  <div class="stage-photo" role="img" aria-label="Dim stage photograph of dancers under coloured lights"></div>

  <header>
    <div class="brand"><span class="brand-dot"></span><span class="brand-name">Velluta Strambo</span></div>
    <div class="search">
      <span>Search</span>
      <svg width="14" height="14" viewBox="0 0 14 14"><circle cx="5.5" cy="5.5" r="4" fill="none" stroke="#111" stroke-width="2"/><line x1="8.5" y1="8.5" x2="12.5" y2="12.5" stroke="#111" stroke-width="2.4" stroke-linecap="round"/></svg>
    </div>
    <nav class="main-nav">
      <a class="current" href="#" style="left:65px">HOME</a>
      <a href="#" style="left:179px">ABOUT</a>
      <a href="#" style="left:296px">SHOWS</a>
      <a href="#" style="left:422px">COMPANY</a>
      <a href="#" style="left:552px">GALLERY</a>
      <a href="#" style="left:689px">PROMOREEL</a>
      <a href="#" style="left:826px">CONTACT</a>
    </nav>
  </header>

  <main class="feature-panel">
    <div class="feature-inner">
      <div class="section-links">
        <a href="#" style="top:40px;width:306px">SHOWS</a>
        <a href="#" style="top:92px;width:268px">COMPANY</a>
        <a href="#" style="top:144px;width:293px">GALLERY</a>
        <a href="#" style="top:194px;width:306px">PROMOREEL</a>
      </div>
      <div class="ticket-art" role="img" aria-label="Vintage show ticket illustration for March 10th and April 14th performances"><span>BUY TICKETS</span></div>
      <div class="stage-shot" role="img" aria-label="Black and white photo of a dancer in a hat seen from behind"></div>
    </div>
  </main>

  <footer>
    <p class="site-footer">COPYRIGHT&nbsp; 2013 VELLUTA STRAMBO. ALL RIGHTS RESERVED . | PRIVACY POLICY | PURCHASE POLICY</p>
    <span class="social" style="left:1014px"></span>
    <span class="social" style="left:1039px"></span>
  </footer>
  <div class="bottom-rule"></div>
</body>
</html>
```